Process Flow Chart for Real Estate Agency

We need a visual flow chart of the process of selling a home for our Real Estate Agency. This visual will be provided to all new staff to explain the process and also to potential clients to explain how detailed the process is. It needs to show each step as detailed in the attached word doc and use icons and arrows to show the direction of flow.

Target Market(s)

Staff & Potential Clients

Industry/Entity Type

Real Estate

Font styles to use
Sans Serif

Colors

Designer to choose colors to be used in the design.

Requirements
Must have
• Easy to read, lots of icons, colour coded with Agent in one colour, Admin in another (some tasks are either/or so not sure what to colour those ones.)
Nice to have
• Include one of the two attached logos

```html
<!DOCTYPE html>
<html lang="en">
<head>
<meta charset="utf-8">
<title>Selling Process Flow – Agent &amp; Admin Steps</title>
<link href="https://fonts.googleapis.com/css2?family=Lato:wght@400;700;900&display=swap" rel="stylesheet">
<style>
  :root{
    --backdrop:#e4e4e4;
    --page:#fbfbfb;
    --page-tint:#eeeeee;
    --ink:#2f3236;
    --agent:#2b8ad4;
    --admin:#f39200;
    --lawn:#5c9a3a;
    --sky:#4d8fd0;
    --house:#7e8fa3;
  }
  *{box-sizing:border-box;margin:0;padding:0}
  html,body{width:1200px;height:799px;overflow:hidden;background:var(--backdrop)}
  body{font-family:"Lato",Arial,sans-serif;color:var(--ink)}
  .spread{position:absolute;left:20px;top:191px;width:1160px;height:416px;display:flex;box-shadow:0 4px 14px rgba(0,0,0,.12)}
  .page{position:relative;width:580px;height:416px;background:var(--page);overflow:hidden}
  .page--left{border-right:1px solid #dcdcdc}
  .page-texture{position:absolute;inset:0;background:linear-gradient(160deg,var(--page) 0%,var(--page-tint) 55%,var(--page) 100%);opacity:.8}
  .photo{position:absolute;width:161px;height:116px;background:linear-gradient(180deg,var(--sky) 0%,#9fc3e4 38%,var(--house) 39%,#9aa6b2 68%,var(--lawn) 69%,#4b8530 100%)}
  .page--left .photo{left:21px}
  .page--right .photo{left:398px;width:156px}
  .step{position:absolute;display:flex;align-items:center;gap:10px;font-size:9.2px;font-weight:700;line-height:1.3;letter-spacing:.05px}
  .page--left .step{left:201px;width:370px}
  .page--right .step{left:24px;width:365px}
  .step-icon{flex:0 0 26px;width:26px;height:26px;border-radius:50%;display:flex;align-items:center;justify-content:center;color:#fff;font-size:6.5px;font-weight:900}
  .step-icon svg{width:15px;height:15px}
  .step-icon--agent{background:var(--agent)}
  .step-icon--admin{background:var(--admin)}
  .step-icon--shared{background:linear-gradient(135deg,var(--agent) 50%,var(--admin) 50%)}
  .role-agent{color:var(--agent)}
  .role-admin{color:var(--admin)}
  .folio{position:absolute;bottom:4px;font-size:5px;color:#666}
</style>
</head>
<body>
<svg width="0" height="0" style="position:absolute">
  <defs>
    <symbol id="ic-person" viewBox="0 0 16 16"><circle cx="8" cy="5" r="3" fill="none" stroke="#fff" stroke-width="1.3"/><path d="M2.5 14c0-3 2.5-5 5.5-5s5.5 2 5.5 5" fill="none" stroke="#fff" stroke-width="1.3"/></symbol>
    <symbol id="ic-group" viewBox="0 0 16 16"><circle cx="5" cy="5" r="2" fill="none" stroke="#fff" stroke-width="1.2"/><circle cx="11" cy="5" r="2" fill="none" stroke="#fff" stroke-width="1.2"/><path d="M1.5 13c0-2 1.5-4 3.5-4s3.5 2 3.5 4M7.5 13c0-2 1.5-4 3.5-4s3.5 2 3.5 4" fill="none" stroke="#fff" stroke-width="1.2"/></symbol>
    <symbol id="ic-card" viewBox="0 0 16 16"><rect x="2" y="3" width="12" height="10" rx="1.5" fill="none" stroke="#fff" stroke-width="1.2"/><circle cx="6" cy="7" r="1.5" fill="#fff"/><path d="M9 6.5h3.5M9 9h3.5M4 11h4" stroke="#fff" stroke-width="1"/></symbol>
    <symbol id="ic-calendar" viewBox="0 0 16 16"><rect x="2" y="3" width="12" height="11" rx="1" fill="none" stroke="#fff" stroke-width="1.2"/><path d="M2 6.5h12M5 2v2.5M11 2v2.5M6 6.5v7.5M10 6.5v7.5M2 10h12" stroke="#fff" stroke-width="1"/></symbol>
    <symbol id="ic-list" viewBox="0 0 16 16"><path d="M5 5h9M5 8.5h9M5 12h9" stroke="#fff" stroke-width="1.4"/><circle cx="2.5" cy="5" r="1" fill="#fff"/><circle cx="2.5" cy="8.5" r="1" fill="#fff"/><circle cx="2.5" cy="12" r="1" fill="#fff"/></symbol>
    <symbol id="ic-doc" viewBox="0 0 16 16"><path d="M4 2h6l3 3v9H4z" fill="none" stroke="#fff" stroke-width="1.2"/><path d="M6 7h5M6 9.5h5M6 12h3" stroke="#fff" stroke-width="1"/></symbol>
    <symbol id="ic-deliver" viewBox="0 0 16 16"><rect x="2" y="3" width="9" height="10" rx="1" fill="none" stroke="#fff" stroke-width="1.2"/><circle cx="11.5" cy="11" r="3" fill="none" stroke="#fff" stroke-width="1.2"/><path d="M11.5 9.5v3M10 11h3" stroke="#fff" stroke-width="1"/></symbol>
    <symbol id="ic-chart" viewBox="0 0 16 16"><rect x="2" y="3" width="12" height="9" fill="none" stroke="#fff" stroke-width="1.2"/><path d="M4 10l3-3 2 2 3-3M6 14h4" stroke="#fff" stroke-width="1.1" fill="none"/></symbol>
    <symbol id="ic-book" viewBox="0 0 16 16"><rect x="2" y="3" width="5.5" height="10" fill="none" stroke="#fff" stroke-width="1.2"/><rect x="8.5" y="3" width="5.5" height="10" fill="none" stroke="#fff" stroke-width="1.2"/><path d="M3.5 6h2.5M10 6h2.5" stroke="#fff"/></symbol>
    <symbol id="ic-star" viewBox="0 0 16 16"><circle cx="8" cy="8" r="6" fill="none" stroke="#fff" stroke-width="1.2"/><path d="M8 4.5l1 2.2 2.4.2-1.8 1.6.5 2.4L8 9.7l-2.1 1.2.5-2.4L4.6 6.9 7 6.7z" fill="none" stroke="#fff" stroke-width=".9"/></symbol>
    <symbol id="ic-pen" viewBox="0 0 16 16"><path d="M3 2h7l3 3v9H3z" fill="none" stroke="#fff" stroke-width="1.2"/><path d="M6 11l5-5 1 1-5 5H6z" fill="#fff"/></symbol>
    <symbol id="ic-folder" viewBox="0 0 16 16"><path d="M2 4h4l1.5 1.5H14V13H2z" fill="none" stroke="#fff" stroke-width="1.2"/><path d="M5 9h6" stroke="#fff" stroke-width="1.1"/></symbol>
  </defs>
</svg>

<main class="spread">
  <section class="page page--left">
    <div class="page-texture" role="img" aria-label="Faint line-drawn streetscape of houses and trees as page background"></div>
    <div class="photo" style="top:21px" role="img" aria-label="Photo of a navy craftsman house with stone pathway and lawn"></div>
    <div class="photo" style="top:150px" role="img" aria-label="Photo of a blue two-storey house with white trim and lawn"></div>
    <div class="photo" style="top:280px" role="img" aria-label="Photo of a grey suburban house with garden path"></div>

    <div class="step" style="top:15px"><span class="step-icon step-icon--agent"><svg><use href="#ic-person"/></svg></span><p>1. <span class="role-agent">Agent</span> calls potential client to arrange a time to meet and obtain details about the property</p></div>
    <div class="step" style="top:54px"><span class="step-icon step-icon--agent"><svg><use href="#ic-group"/></svg></span><p>2. <span class="role-agent">Agent</span> ensures all decision makers will be present at meeting</p></div>
    <div class="step" style="top:93px"><span class="step-icon step-icon--agent"><svg><use href="#ic-card"/></svg></span><p>3. <span class="role-agent">Agent</span> adds vendors contact details on phone</p></div>
    <div class="step" style="top:133px"><span class="step-icon step-icon--agent"><svg><use href="#ic-calendar"/></svg></span><p>4. <span class="role-agent">Agent</span> adds appointment to personal calendar</p></div>
    <div class="step" style="top:172px"><span class="step-icon step-icon--agent">SMS</span><p>5. <span class="role-agent">Agent</span> sends SMS to potential client to thank them for the opportunity</p></div>
    <div class="step" style="top:212px"><span class="step-icon step-icon--shared"><svg><use href="#ic-list"/></svg></span><p>6. <span class="role-agent">Agent</span>/<span class="role-admin">Admin</span> orders ARE from Harrowfield's</p></div>
    <div class="step" style="top:253px"><span class="step-icon step-icon--agent"><svg><use href="#ic-list"/></svg></span><p>7. <span class="role-agent">Agent</span> completes a TMP to provide to Admin for Prelisting kit prep</p></div>
    <div class="step" style="top:291px"><span class="step-icon step-icon--admin"><svg><use href="#ic-book"/></svg></span><p>8. <span class="role-admin">Admin</span> prepares pre-listing kit with questionnaire, sample brochure &amp; cover letter, property magazine, agent profile booklet</p></div>
    <div class="step" style="top:331px"><span class="step-icon step-icon--shared"><svg><use href="#ic-deliver"/></svg></span><p>9. <span class="role-admin">Admin</span>/<span class="role-agent">Agent</span> delivers pre-listing kit (preferably within the hour) &amp; SMS potential vendor</p></div>
    <div class="step" style="top:370px"><span class="step-icon step-icon--shared"><svg><use href="#ic-chart"/></svg></span><p>10. <span class="role-admin">Admin</span>/<span class="role-agent">Agent</span> to research &amp; prints comparable Sales reports</p></div>
    <span class="folio" style="left:10px">1</span>
  </section>

  <section class="page page--right">
    <div class="page-texture" role="img" aria-label="Faint line-drawn streetscape of houses and trees as page background"></div>
    <div class="photo" style="top:21px" role="img" aria-label="Photo of a grey house with garage under blue sky"></div>
    <div class="photo" style="top:150px" role="img" aria-label="Photo of a stone and cream two-storey house"></div>
    <div class="photo" style="top:280px" role="img" aria-label="Photo of a house with front porch in bright sunlight"></div>

    <div class="step" style="top:15px"><span class="step-icon step-icon--admin"><svg><use href="#ic-book"/></svg></span><p>11. <span class="role-admin">Admin</span> prepares TMP with Marketing Costs Selection booklet, Service Offering Selection booklet, Sales Agency Agreement &amp; Benefits Form, ARE</p></div>
    <div class="step" style="top:54px"><span class="step-icon step-icon--admin"><svg><use href="#ic-star"/></svg></span><p>12. <span class="role-admin">Admin</span> enters potential Vendor into CRM &amp; set “Appraisal” Track</p></div>
    <div class="step" style="top:93px"><span class="step-icon step-icon--agent"><svg><use href="#ic-star"/></svg></span><p>13. <span class="role-agent">Agent</span> confirms appraisal on the morning of the appointment with an SMS</p></div>
    <div class="step" style="top:133px"><span class="step-icon step-icon--agent"><svg><use href="#ic-group"/></svg></span><p>14. <span class="role-agent">Agent</span> meets with potential Vendor and completes the appraisal</p></div>
    <div class="step" style="top:172px"><span class="step-icon step-icon--admin"><svg><use href="#ic-doc"/></svg></span><p>15. <span class="role-admin">Admin</span> prepares written appraisal report hand-deliver with coffee vouchers &amp;/or gift</p></div>
    <div class="step" style="top:212px"><span class="step-icon step-icon--admin"><svg><use href="#ic-doc"/></svg></span><p>16. <span class="role-agent">Agent</span> hand-delivers report with coffee voucher or Calder chocolates</p></div>
    <div class="step" style="top:253px"><span class="step-icon step-icon--admin"><svg><use href="#ic-pen"/></svg></span><p>17. <span class="role-agent">Agent</span> receives confirmation from vendor to proceed with listing &amp; arranges signing of Residential Sales Agency Agreement</p></div>
    <div class="step" style="top:291px"><span class="step-icon step-icon--admin"><svg><use href="#ic-list"/></svg></span><p>18. <span class="role-admin">Admin</span> checks Residential Sales Agency &amp; enters as Listing into CRM</p></div>
    <div class="step" style="top:331px"><span class="step-icon step-icon--admin"><svg><use href="#ic-folder"/></svg></span><p>19. <span class="role-admin">Admin</span> completes the “New Listing Checklist” and prepares black folder</p></div>
    <div class="step" style="top:370px"><span class="step-icon step-icon--admin" style="font-size:14px">@</span><p>20. <span class="role-admin">Admin</span> checks for Vendor email addresses &amp; if required call or SMS client to obtain</p></div>
    <span class="folio" style="right:10px">2</span>
  </section>
</main>
</body>
</html>
```